Business Card for KV

We need a double sided business card:

First Name Last Name
Cell 987-605-3214
mailbox@pelvaro-post.com

License #8096-WXYZ-2318
WFLMA # 60782
Dunmere County

```html
<!DOCTYPE html>
<html lang="en">
<head>
<meta charset="utf-8">
<title>Kestrel Vale – Business Card</title>
<link rel="stylesheet" href="https://fonts.googleapis.com/css2?family=Staatliches&display=swap">
<style>
  :root {
    --stage: #3b3b3b;
    --card: #ffffff;
    --navy: #2c4a6b;
    --olive: #8e9146;
    --radius: 40px;
  }
  * { box-sizing: border-box; margin: 0; padding: 0; }
  html, body {
    width: 1189px; height: 1200px; overflow: hidden;
    background: var(--stage);
    font-family: "Staatliches", sans-serif;
  }
  .stage { position: relative; width: 1189px; height: 1200px; }
  .card {
    position: absolute; top: 260px;
    width: 480px; height: 680px;
    background: var(--card);
    border-radius: var(--radius);
    display: flex; flex-direction: column; align-items: center; justify-content: center;
    text-align: center;
  }
  .card--back { left: 80px; }
  .card--front { left: 629px; }

  .contact { width: 300px; display: flex; flex-direction: column; align-items: center; }
  .contact__name { color: var(--navy); font-size: 46px; letter-spacing: 1px; line-height: 1; font-weight: 400; }
  .contact__title { color: var(--olive); font-size: 22px; letter-spacing: 1px; margin-top: 4px; }
  .contact__label {
    display: flex; align-items: center; gap: 14px; width: 100%;
    color: var(--olive); font-size: 18px; letter-spacing: 1px; margin-top: 18px;
  }
  .contact__label::before, .contact__label::after {
    content: ""; flex: 1; height: 1.5px; background: var(--olive);
  }
  .contact__value { color: var(--navy); font-size: 24px; letter-spacing: 1px; line-height: 1.1; }
  .contact__value--email { font-size: 20px; }
  .contact__legal { color: var(--navy); font-size: 22px; letter-spacing: 1px; line-height: 1.15; margin-top: 20px; }
  .contact__rule { width: 100%; height: 1.5px; background: var(--olive); margin-top: 14px; }
  .contact__leaf {
    width: 90px; height: 28px; margin-top: 4px;
    background: linear-gradient(180deg, var(--olive), #b3b67a);
    border-radius: 0 0 45px 45px;
  }

  .brand { display: flex; flex-direction: column; align-items: center; gap: 18px; margin-top: -40px; }
  .brand__dot { width: 84px; height: 84px; border-radius: 50%; background: var(--olive); }
  .brand__name { color: var(--navy); font-size: 54px; letter-spacing: 3px; line-height: 1; }
</style>
</head>
<body>
  <main class="stage">
    <section class="card card--back" aria-label="Card back">
      <div class="contact">
        <h1 class="contact__name">Marel Osk</h1>
        <p class="contact__title">Manager</p>
        <p class="contact__label">Cell</p>
        <p class="contact__value">987-605-3214</p>
        <p class="contact__label">Email</p>
        <p class="contact__value contact__value--email">mailbox@pelvaro-post.com</p>
        <p class="contact__legal">License #8096-WXYZ-2318<br>WFLMA # 60782<br>Dunmere County</p>
        <div class="contact__rule"></div>
        <div class="contact__leaf" role="img" aria-label="Small leaf ornament"></div>
      </div>
    </section>

    <section class="card card--front" aria-label="Card front">
      <div class="brand">
        <span class="brand__dot"></span>
        <p class="brand__name">Kestrel Vale</p>
      </div>
    </section>
  </main>
</body>
</html>
```